Residential Construction Company needs flyer designed.

We need a flyer design for a residential Rain Gutter and Screen room company. We have over 50 years in the remodeling industry and service all of Middle Georgia. We want the brochure to highlight our wonderful managerial staff to our great instillation crews. We also want to showcase the high-quality products that we use, gutter, leaf protection, screen rooms and sunrooms and the quality craftsmanship homeowners will receive when they choose to go with our company.

```html
<!DOCTYPE html>
<html lang="en">
<head>
<meta charset="utf-8">
<title>Hartwell Gutters &amp; Exteriors – Residential Flyer</title>
<link href="https://fonts.googleapis.com/css2?family=Poppins:wght@400;500;600;700&family=Ultra&display=swap" rel="stylesheet">
<style>
  :root{
    --navy:#1b2b3e;
    --navy-deep:#14202f;
    --teal:#14a5a0;
    --teal-dark:#0f8a89;
    --green:#13a097;
    --blue:#1e4f9e;
    --bar-blue:#2170c4;
    --yellow:#f3e51d;
    --white:#ffffff;
    --sky-1:#3f8ee0;
    --sky-2:#b9dcf6;
  }
  *{box-sizing:border-box;margin:0;padding:0}
  html,body{width:847px;height:1200px;overflow:hidden;background:#e9ecef}
  .flyer{position:relative;width:847px;height:1200px;overflow:hidden;background:var(--navy);font-family:'Poppins',sans-serif;color:var(--white)}
  .layer{position:absolute;left:0;top:0}
  .brand{position:absolute;left:56px;top:52px;display:flex;align-items:center;gap:10px;font-family:'Poppins',sans-serif;font-weight:700;color:var(--blue);font-size:21px;line-height:1}
  .brand-dot{width:16px;height:16px;border-radius:50%;background:var(--blue)}
  .headline{position:absolute;left:56px;top:124px}
  .headline .kicker{font-weight:700;color:var(--green);font-size:32px;line-height:36px;letter-spacing:.3px}
  .headline .title{font-family:'Ultra',serif;color:var(--blue);font-size:43px;line-height:47px;letter-spacing:.5px}
  .headline .company{font-weight:400;color:var(--navy-deep);font-size:29px;letter-spacing:9px;line-height:36px;margin-top:2px}
  .mission{position:absolute;left:56px;top:312px;width:300px;padding-left:12px;border-left:3px solid var(--yellow);color:var(--navy-deep);font-size:17.5px;line-height:23px;font-weight:500}
  .gutter-callout{position:absolute;left:508px;top:330px;width:268px;height:150px;background:var(--navy);border-radius:10px;transform:rotate(-5deg);padding:42px 0 0 24px}
  .gutter-callout .small{font-size:19px;line-height:22px;color:var(--white)}
  .gutter-callout .big{font-family:'Ultra',serif;color:var(--yellow);font-size:40px;line-height:46px}
  .services{position:absolute;left:56px;top:500px}
  .services h2{font-family:'Ultra',serif;font-weight:400;font-size:33px;line-height:50px;color:var(--white)}
  .services h2 span{color:var(--yellow)}
  .service-list{list-style:none;margin-top:18px}
  .service-list li{display:flex;align-items:center;height:53.5px;font-size:22px;font-weight:500}
  .service-icon{width:38px;height:38px;border-radius:50%;margin-right:20px;flex:none;display:flex;align-items:center;justify-content:center}
  .service-icon.blue{background:var(--bar-blue)}
  .service-icon.teal{background:var(--teal)}
  .products-bar{position:absolute;left:381px;top:512px;width:466px;height:39px;background:var(--bar-blue);border-radius:6px 0 0 6px;font-weight:700;font-size:19.5px;line-height:39px;padding-left:22px}
  .product-label{position:absolute;font-weight:700;font-size:15px;line-height:17px;color:var(--white);text-align:center}
  .experience{position:absolute;right:149px;top:1010px;width:320px;text-align:right;font-size:13.5px;line-height:17px;font-weight:500;text-transform:uppercase;color:var(--white)}
  .badge{position:absolute;left:714px;top:1005px;width:78px;height:78px;border-radius:50%;background:var(--navy-deep);border:4px solid #d9b540;display:flex;flex-direction:column;align-items:center;justify-content:center;color:#e8c653}
  .badge .num{font-weight:700;font-size:28px;line-height:26px}
  .badge .yrs{font-weight:600;font-size:11px;line-height:12px}
  .call{position:absolute;left:442px;top:1074px;display:flex;align-items:center;font-weight:700;font-size:24px;color:var(--navy-deep);white-space:nowrap}
  .call .phone{display:flex;align-items:center;color:var(--white);margin-left:14px;font-size:25px}
  .call .phone svg{margin-right:6px}
  .web-bar{position:absolute;left:447px;top:1122px;width:400px;height:32px;background:var(--navy);border-radius:8px 0 0 8px;font-size:15.5px;line-height:32px;letter-spacing:1.2px;padding-left:26px;font-weight:500}
</style>
</head>
<body>
<main class="flyer">

  <svg class="layer" width="847" height="1200" viewBox="0 0 847 1200" aria-hidden="false">
    <defs>
      <linearGradient id="skyGrad" x1="0" y1="0" x2="1" y2="0.4">
        <stop offset="0" stop-color="#eaf4fc"/>
        <stop offset=".45" stop-color="var(--sky-2)"/>
        <stop offset="1" stop-color="var(--sky-1)"/>
      </linearGradient>
      <linearGradient id="whiteFade" x1="0" y1="0" x2="1" y2="0">
        <stop offset="0" stop-color="#fff"/>
        <stop offset=".72" stop-color="#fff"/>
        <stop offset="1" stop-color="#fff" stop-opacity="0"/>
      </linearGradient>
      <linearGradient id="roofGrad" x1="0" y1="0" x2="1" y2="1">
        <stop offset="0" stop-color="#8a6656"/>
        <stop offset=".6" stop-color="#6b4e44"/>
        <stop offset="1" stop-color="#b8965a"/>
      </linearGradient>
      <linearGradient id="tealGrad" x1="0" y1="0" x2="0" y2="1">
        <stop offset="0" stop-color="var(--teal)"/>
        <stop offset="1" stop-color="var(--teal-dark)"/>
      </linearGradient>
      <linearGradient id="houseGrad" x1="0" y1="0" x2="0" y2="1">
        <stop offset="0" stop-color="#5a6370"/>
        <stop offset=".5" stop-color="#e8e6e1"/>
        <stop offset="1" stop-color="#6f7b5a"/>
      </linearGradient>
      <linearGradient id="photoGrad" x1="0" y1="0" x2="0" y2="1">
        <stop offset="0" stop-color="#a9c8e4"/>
        <stop offset=".5" stop-color="#8a7a6a"/>
        <stop offset="1" stop-color="#5d7a4a"/>
      </linearGradient>
      <linearGradient id="smallGrad" x1="0" y1="0" x2="0" y2="1">
        <stop offset="0" stop-color="#6d737a"/>
        <stop offset="1" stop-color="#4b5a56"/>
      </linearGradient>
    </defs>

    <!-- sky backdrop -->
    <rect role="img" aria-label="Blue sky with light clouds" x="0" y="0" width="847" height="470" fill="url(#skyGrad)"/>

    <!-- roof with worker -->
    <path role="img" aria-label="Photo of a worker pressure washing a tiled roof above a gutter" d="M470 320 L640 150 L847 20 V420 H560 Z" fill="url(#roofGrad)"/>

    <!-- teal product panel -->
    <path d="M352 430 C 420 405 470 405 520 420 L847 400 V1200 H352 Z" fill="url(#tealGrad)"/>

    <!-- white heading panel -->
    <path d="M0 0 H540 C 505 150 500 300 440 380 C 400 430 330 468 250 474 C 160 480 80 468 0 438 Z" fill="url(#whiteFade)"/>

    <!-- bottom-left house photo -->
    <path role="img" aria-label="Photo of a large white brick two-storey home" d="M0 1000 L90 960 L210 950 L300 975 L412 1060 V1200 H0 Z" fill="url(#houseGrad)"/>

    <!-- product circles -->
    <g stroke="var(--teal-dark)" stroke-width="6">
      <circle role="img" aria-label="Close-up photo of a roof edge gutter" cx="460" cy="653" r="78" fill="url(#smallGrad)"/>
      <circle role="img" aria-label="Photo of a home sunroom addition" cx="715" cy="653" r="78" fill="url(#smallGrad)"/>
      <circle role="img" aria-label="Photo of a screen room porch" cx="460" cy="880" r="78" fill="url(#smallGrad)"/>
      <circle role="img" aria-label="Photo of leaf protection on a gutter" cx="715" cy="880" r="78" fill="url(#smallGrad)"/>
    </g>
    <circle role="img" aria-label="Photo of a craftsman-style home with new gutters" cx="588" cy="770" r="130" fill="url(#photoGrad)" stroke="var(--bar-blue)" stroke-width="5"/>

    <!-- curved arrow toward roof -->
    <path d="M560 318 C 545 270 555 235 585 215" fill="none" stroke="var(--yellow)" stroke-width="4" stroke-linecap="round"/>
    <path d="M570 212 L588 213 L583 230" fill="none" stroke="var(--yellow)" stroke-width="4" stroke-linecap="round" stroke-linejoin="round"/>
  </svg>

  <div class="brand"><span class="brand-dot"></span>Hartwell Gutters &amp; Exteriors</div>

  <header class="headline">
    <p class="kicker">RESIDENTIAL</p>
    <h1 class="title">RAIN GUTTER &amp;<br>SCREEN ROOM</h1>
    <p class="company">COMPANY</p>
  </header>

  <p class="mission">Our mission is to provide each customer with an excellent product, superior service and quality workmanship.</p>

  <div class="gutter-callout">
    <p class="small">Thinking of<br>cleaning your</p>
    <p class="big">Gutter?</p>
  </div>
  <svg class="layer" width="847" height="1200" style="pointer-events:none">
    <circle role="img" aria-label="Photo of hands clearing debris from a gutter" cx="718" cy="300" r="58" fill="url(#smallGrad)" stroke="var(--navy)" stroke-width="5"/>
  </svg>

  <section class="services">
    <h2>Our <span>Services</span></h2>
    <ul class="service-list">
      <li><span class="service-icon blue"><svg width="20" height="20" viewBox="0 0 20 20"><path d="M3 16 H17 M6 16 V8 L10 4 L14 8 V16" fill="none" stroke="#fff" stroke-width="2"/></svg></span>Gutter system</li>
      <li><span class="service-icon teal"><svg width="20" height="20" viewBox="0 0 20 20"><rect x="4" y="5" width="12" height="10" fill="none" stroke="#fff" stroke-width="2"/><path d="M4 10 H16" stroke="#fff" stroke-width="2"/></svg></span>Gutter cleaning</li>
      <li><span class="service-icon blue"><svg width="22" height="22" viewBox="0 0 22 22"><circle cx="11" cy="11" r="4" fill="#fff"/><path d="M11 2 V5 M11 17 V20 M2 11 H5 M17 11 H20 M4.6 4.6 L6.7 6.7 M15.3 15.3 L17.4 17.4 M4.6 17.4 L6.7 15.3 M15.3 6.7 L17.4 4.6" stroke="#fff" stroke-width="2"/></svg></span>Sunroom</li>
      <li><span class="service-icon teal"><svg width="20" height="20" viewBox="0 0 20 20"><path d="M5 3 V17 H15 M9 7 H13 V14" fill="none" stroke="#fff" stroke-width="2"/></svg></span>Gutter protection</li>
      <li><span class="service-icon blue"><svg width="20" height="20" viewBox="0 0 20 20"><path d="M2 8 L10 3 L18 8 Z M5 8 V17 M15 8 V17 M7 12 H13 M8 12 V16 M12 12 V16" fill="none" stroke="#fff" stroke-width="1.8"/></svg></span>Patio covers</li>
      <li><span class="service-icon teal"><svg width="20" height="20" viewBox="0 0 20 20"><path d="M4 17 V8 L10 3 L16 8 V17 Z M10 8 V17 M4 12 H16" fill="none" stroke="#fff" stroke-width="1.8"/></svg></span>Screen rooms</li>
      <li><span class="service-icon blue"><svg width="20" height="20" viewBox="0 0 20 20"><rect x="4" y="3" width="12" height="14" fill="none" stroke="#fff" stroke-width="2"/><path d="M8 6 V14 M12 6 V14" stroke="#fff" stroke-width="1.6"/></svg></span>Vinyl film windows</li>
    </ul>
  </section>

  <div class="products-bar">Our high-quality products that we use</div>
  <p class="product-label" style="left:420px;top:627px;width:80px">GUTTER</p>
  <p class="product-label" style="left:662px;top:627px;width:110px">SUNROOMS</p>
  <p class="product-label" style="left:410px;top:862px;width:100px">SCREEN<br>ROOMS</p>
  <p class="product-label" style="left:655px;top:862px;width:120px">LEAF<br>PROTECTION</p>

  <p class="experience">We have over 50 years in the remodeling industry and service all of Middle Georgia.</p>
  <div class="badge"><span class="num">50</span><span class="yrs">YEARS</span></div>

  <div class="call">CALL US AT:
    <span class="phone"><svg width="24" height="24" viewBox="0 0 24 24"><circle cx="12" cy="12" r="11" fill="var(--yellow)"/><path d="M8 6.5 L10 6.5 L11 9.5 L9.7 10.6 C10.4 12 11.8 13.5 13.4 14.3 L14.5 13 L17.5 14 V16 C17.5 16.8 16.8 17.5 16 17.5 C11 17 7 13 6.5 8 C6.5 7.2 7.2 6.5 8 6.5 Z" fill="var(--navy)"/></svg>478.555.0142</span>
  </div>

  <div class="web-bar">www.hartwellguttersandexteriors.com</div>
</main>
</body>
</html>
```